Attorney business card for two offices

Looking for a new business card design that can list both of my offices, one in Houston and one in West Texas. Want something masculine, easy to read, and conservative yet somewhat modern. Our current card has used a nautical star on it for years, but I am not necessarily attached to that. Also, a lot of our forms use dark green and orange. Second office address is P.O. Box 518, Marathon, Texas 79615

```html
<!DOCTYPE html>
<html lang="en">
<head>
<meta charset="utf-8">
<title>Hale Law Firm – Business Card</title>
<link href="https://fonts.googleapis.com/css2?family=Cinzel:wght@500;600;700&family=Tinos&display=swap" rel="stylesheet">
<style>
  :root {
    --backdrop: #dcdcdc;
    --firm-green: #14673a;
    --firm-orange: #f07f1a;
    --paper: #ffffff;
    --ink-green: #1b5e35;
  }
  * { margin: 0; padding: 0; box-sizing: border-box; }
  html, body { width: 1200px; height: 800px; overflow: hidden; }
  body {
    position: relative;
    background: var(--backdrop);
    font-family: "Tinos", "Times New Roman", serif;
  }
  .card {
    position: absolute;
    top: 283px;
    width: 429px;
    height: 239px;
  }
  .card-front { left: 111px; background: var(--firm-green); }
  .card-back  { left: 638px; background: var(--paper); overflow: hidden; }

  .firm-name {
    position: absolute;
    display: flex;
    align-items: center;
    gap: 10px;
    font-family: "Cinzel", Georgia, serif;
    font-weight: 600;
    white-space: nowrap;
  }
  .firm-mark { display: block; width: 14px; height: 14px; background: var(--firm-orange); }
  .card-front .firm-name {
    left: 0; right: 0; top: 105px;
    justify-content: center;
    color: var(--paper);
    font-size: 22px;
    letter-spacing: 0.5px;
  }
  .card-back .firm-name {
    left: 27px; top: 34px;
    color: var(--firm-green);
    font-size: 21px;
    letter-spacing: 0.5px;
  }

  .attorney-name {
    position: absolute;
    left: 27px; top: 120px;
    font-family: "Cinzel", Georgia, serif;
    font-weight: 600;
    font-size: 14px;
    color: var(--ink-green);
    letter-spacing: 0.3px;
  }
  .attorney-title {
    position: absolute;
    left: 27px; top: 138px;
    font-size: 11px;
    color: var(--firm-orange);
  }
  .title-rule {
    position: absolute;
    left: 107px; right: 27px; top: 147px;
    height: 1px;
    background: var(--firm-green);
  }
  .contact-list {
    position: absolute;
    left: 27px; top: 158px;
    list-style: none;
  }
  .contact-list li {
    display: flex;
    align-items: center;
    gap: 6px;
    font-size: 10.5px;
    color: var(--ink-green);
    height: 16.5px;
  }
  .icon { width: 10px; height: 10px; flex: none; }

  .office-list {
    position: absolute;
    left: 265px; top: 158px;
    list-style: none;
  }
  .office-address {
    display: flex;
    align-items: flex-start;
    gap: 6px;
    font-size: 10.5px;
    line-height: 15px;
    color: var(--ink-green);
    white-space: nowrap;
  }
  .office-address + .office-address { margin-top: 4px; }
  .office-address .icon { width: 10px; height: 13px; margin-top: 1px; }

  .stripe-orange {
    position: absolute; left: 0; right: 0; top: 227px;
    height: 2px; background: var(--firm-orange);
  }
  .stripe-green {
    position: absolute; left: 0; right: 0; top: 232px;
    height: 7px; background: var(--firm-green);
  }
</style>
</head>
<body>

  <section class="card card-front" aria-label="Card front">
    <div class="firm-name"><span class="firm-mark"></span>Hale Law Firm, P.C</div>
  </section>

  <section class="card card-back" aria-label="Card back">
    <div class="firm-name"><span class="firm-mark"></span>Hale Law Firm, P.C</div>

    <div class="attorney-name">Daniel R, Hale, Sr</div>
    <div class="attorney-title">Attorney At law</div>
    <div class="title-rule"></div>

    <ul class="contact-list">
      <li>
        <svg class="icon" viewBox="0 0 10 10" aria-hidden="true"><path fill="#f07f1a" d="M1 3c0-1 1-2 4-2s4 1 4 2v1H7V3H3v1H1zM2 5h6l1 4H1z"/></svg>
        (713) 555-0142
      </li>
      <li>
        <svg class="icon" viewBox="0 0 10 10" aria-hidden="true"><path fill="#f07f1a" d="M3 0h4v3H3zM0 3.5h10v4H8V6H2v1.5H0zM2.5 6.5h5V10h-5z"/></svg>
        (832) 555-0178
      </li>
      <li>
        <svg class="icon" viewBox="0 0 10 10" aria-hidden="true"><path fill="#f07f1a" d="M0 2h10v6H0z"/><path fill="none" stroke="#fff" stroke-width="1" d="M0.5 2.5 5 6l4.5-3.5"/></svg>
        daniel@haletexlaw.com
      </li>
    </ul>

    <ul class="office-list">
      <li class="office-address">
        <svg class="icon" viewBox="0 0 10 13" aria-hidden="true"><path fill="#f07f1a" d="M5 0a5 5 0 0 0-5 5c0 3.5 5 8 5 8s5-4.5 5-8a5 5 0 0 0-5-5zm0 7a2 2 0 1 1 0-4 2 2 0 0 1 0 4z"/></svg>
        <span>4410 Elm Freeway, Suite 210<br>Houston, Texas 77055</span>
      </li>
      <li class="office-address">
        <svg class="icon" viewBox="0 0 10 13" aria-hidden="true"><path fill="#f07f1a" d="M5 0a5 5 0 0 0-5 5c0 3.5 5 8 5 8s5-4.5 5-8a5 5 0 0 0-5-5zm0 7a2 2 0 1 1 0-4 2 2 0 0 1 0 4z"/></svg>
        <span>P.O. Box 518<br>Marathon, Texas 79615</span>
      </li>
    </ul>

    <div class="stripe-orange"></div>
    <div class="stripe-green"></div>
  </section>

</body>
</html>
```